Redesign of page from emergency manual

Please redesign this PDF to look better. Please don't include any stock photos. It must be legible. Making some words bold is probably a good idea.

Here are some things I like :

https://tarrowbooks.com.au/collections/frontpage/products/the-plk-v2-ebook

https://img-cd.vostramediafiles.com/qa-ejkwPLOTYY_SuCKbZNu411Qwgjv8YssPxEdzXN93hDkSRjLXK8WmfgbmrJW4ZZ3yUPK=w1052-h592-rw

```html
<!DOCTYPE html>
<html lang="en">
<head>
<meta charset="utf-8">
<title>Hypertension, Acute</title>
<link href="https://fonts.googleapis.com/css2?family=Noto+Sans:ital,wght@0,400;0,600;0,700;0,800;1,400&display=swap" rel="stylesheet">
<style>
:root{
  --cyan:#66eeff;
  --cyan-light:#b5f5ff;
  --paper:#f7feff;
  --ink:#111111;
  --rule:#333333;
  --muted:#8a8a8a;
  --alert:#c0392b;
  --canvas:#ffffff;
}
*{box-sizing:border-box;margin:0;padding:0}
html,body{width:1200px;height:1200px;overflow:hidden;background:var(--canvas)}
body{font-family:"Noto Sans",sans-serif;color:var(--ink);position:relative}
b,strong{font-weight:700}
.page{position:absolute;left:181px;top:76px;width:825px;height:1031px}
.sheet{position:absolute;left:0;top:0;width:737px;height:1031px;background:var(--paper)}
.header{position:absolute;left:0;top:0;width:737px;height:87px;background:var(--cyan)}
.title{position:absolute;left:34px;top:22px;font-size:36px;font-weight:800;letter-spacing:.4px;line-height:1.2}
.header-rule{position:absolute;left:430px;top:31px;width:1px;height:27px;background:var(--rule)}
.subtitle{position:absolute;left:448px;top:28px;font-size:13.5px;line-height:16px}
.tab{position:absolute;left:762px;top:0;width:63px;height:1031px;background:var(--cyan)}
.tab-number{position:absolute;top:40px;width:100%;text-align:center;font-size:27px;font-weight:800}
.tab-title{position:absolute;left:50%;top:287px;transform-origin:0 0;transform:translateX(19px) rotate(90deg);white-space:nowrap;font-size:39px;font-weight:800;line-height:1}
.tab-note{position:absolute;left:50%;top:845px;transform-origin:0 0;transform:translateX(9px) rotate(90deg);white-space:nowrap;font-size:14px;color:var(--muted)}
.intro{position:absolute;left:36px;top:103px;width:365px}
.intro-lead{font-size:16px;line-height:20px;padding-left:17px;position:relative}
.intro-lead::before{content:"";position:absolute;left:0;top:6px;width:8px;height:8px;background:var(--ink)}
.checks{list-style:none;margin-top:16px;font-size:13.7px;line-height:17px;width:340px}
.checks li{margin-bottom:6px;padding-left:9px;position:relative}
.checks li::before{content:"›";position:absolute;left:0;top:0;font-weight:700}
.intro-rule{position:absolute;left:423px;top:107px;width:1px;height:150px;background:var(--rule)}
.bp-table{position:absolute;left:453px;top:105px;width:284px;border-collapse:collapse;font-size:13px;text-align:center}
.bp-table th,.bp-table td{border:1px solid var(--rule);height:29.5px}
.bp-table .bp-caption{height:32px;background:var(--cyan-light)}
.bp-table th{font-weight:700}
.bp-table td.num{font-weight:600}
.caution{position:absolute;left:36px;top:300px;width:600px;font-size:16px;line-height:20.5px}
.caution strong{font-weight:800;font-size:17.5px;color:var(--alert)}
.caution b{font-weight:700}
.drug-table{position:absolute;left:36px;top:418px;width:701px;border-collapse:collapse;font-size:16px;line-height:21px}
.drug-table th,.drug-table td{border:1px solid var(--rule);vertical-align:top}
.drug-table thead th{background:var(--cyan-light);height:44px;vertical-align:middle;font-weight:700}
.drug-table .action{width:179px;padding:16px 10px 0 18px;font-weight:600}
.drug-table .drugs{padding:12px 10px 6px 22px}
.drugs ul{list-style:none}
.drugs li{position:relative;padding-left:17px;margin-bottom:7px}
.drugs li:last-child{margin-bottom:0}
.drugs li::before{content:"";position:absolute;left:0;top:9px;width:4px;height:4px;background:var(--ink)}
.row-1{height:79px}.row-2{height:112px}.row-3{height:77px}.row-4{height:55px}
.row-4 .action{padding-top:6px}
.row-4 .drugs{padding-top:12px}
.ddx{position:absolute;left:36px;top:824px;width:700px}
.ddx-heading{font-size:17.5px;font-weight:800;padding-left:20px;position:relative}
.ddx-heading::before{content:"";position:absolute;left:0;top:11px;width:6px;height:6px;background:var(--ink)}
.ddx-col{position:absolute;top:40px;list-style:none;font-size:16px;line-height:18.5px}
.ddx-col li{padding-left:10px;position:relative;margin-bottom:6px}
.ddx-col li::before{content:"›";position:absolute;left:0;font-weight:700}
.col-a{left:-1px;width:210px}.col-b{left:237px;width:240px}.col-c{left:502px;width:200px}
</style>
</head>
<body>
<div class="page">
  <div class="sheet">
    <div class="header">
      <h1 class="title">Hypertension, Acute</h1>
      <div class="header-rule"></div>
      <p class="subtitle">Sustained high blood pressure<br>refractory to treating reversible causes</p>
    </div>

    <div class="intro">
      <p class="intro-lead">In pediatrics, hypertension is almost always treated by addressing likely causes such a <b>light anesthesia</b> or <b>measurement error</b>:</p>
      <ul class="checks">
        <li>Ensure correct <b>BP cuff size</b>: cuff bladder width ~ 40% of limb circumference</li>
        <li>Ensure <b>arterial line transducer</b> is at level of heart</li>
        <li>Consider placing arterial line if not already present</li>
      </ul>
    </div>
    <div class="intro-rule"></div>

    <table class="bp-table">
      <thead>
        <tr><th colspan="3" class="bp-caption">Hypertensive Blood Pressure Range*</th></tr>
        <tr><th>Age (yr)</th><th>Systolic</th><th>Diastolic</th></tr>
      </thead>
      <tbody>
        <tr><td>newborn</td><td class="num">&gt;97</td><td class="num">&gt;70</td></tr>
        <tr><td>1-3</td><td class="num">&gt;105</td><td class="num">&gt;61</td></tr>
        <tr><td>4-12</td><td class="num">&gt;113</td><td class="num">&gt;86</td></tr>
      </tbody>
    </table>

    <p class="caution"><strong>* CAUTION:</strong> Anti hypertensive drugs are <b>almost never needed</b> for routine pediatric cases. These medications are used almost exclusively for specialized cardiac, neurosurgical, or endocrine (pheochromocytoma) cases. <b>Consult an expert before use. Rule-out increased ICP.</b></p>

    <table class="drug-table">
      <thead><tr><th>Action</th><th>Drug (IV Dosing)</th></tr></thead>
      <tbody>
        <tr class="row-1"><td class="action">Direct smooth muscle relaxation</td>
          <td class="drugs"><ul><li><b>Sodium nitroprusside</b> 0.5-10 MICROgrams/kg/min</li><li><b>HydrALAZINE</b> 0.1-0.2 mg/kg (adult dose 5-10 mg)</li></ul></td></tr>
        <tr class="row-2"><td class="action">β- Adrenergic blockade</td>
          <td class="drugs"><ul><li><b>Esmolol</b> 100-500 MICROgrams/kg over 5 min,<br>then 25-300 MICROgrams/kg/min</li><li><b>Labetalol</b> (also α effect) 0.2-1 mg/kg q 10 min;<br>0.4-3 mg/kg/<em>hour</em> (infusion)</li></ul></td></tr>
        <tr class="row-3"><td class="action">Calcium channel blockade</td>
          <td class="drugs"><ul><li><b>niCARdapine</b> 0.5-5 MICROgrams/kg/min</li><li><b>Clevidipine</b>&nbsp; 0.5-3.5 MICROgrams/kg/min</li></ul></td></tr>
        <tr class="row-4"><td class="action">D1-dopamine agonist</td>
          <td class="drugs"><ul><li><b>Fenoldopam</b>&nbsp; 0.2-0.8 MICROgrams/kg/min</li></ul></td></tr>
      </tbody>
    </table>

    <section class="ddx">
      <h2 class="ddx-heading">Consider Differential (Partial):</h2>
      <ul class="ddx-col col-a">
        <li><b>Light anesthesia</b> (consider vaporizer or infusion pump empty or malfunctioning)</li>
        <li><b>Hypercarbia</b></li>
      </ul>
      <ul class="ddx-col col-b">
        <li><b>Hypoxemia</b></li>
        <li><b>Arterial line transducer</b> too low or BP cuff too small</li>
        <li><b>Withdrawal</b> (EtOH or opioid)</li>
      </ul>
      <ul class="ddx-col col-c">
        <li><b>Thyroid Storm</b></li>
        <li><b>Pheochromocytoma</b></li>
        <li><b>Drug Error</b></li>
      </ul>
    </section>
  </div>

  <aside class="tab">
    <div class="tab-number">12</div>
    <div class="tab-title">Hypertension, Acute</div>
    <div class="tab-note">Critical Events</div>
  </aside>
</div>
</body>
</html>
```